I need a business card design for a new dance business. I offer classical Indian dance tuition and also professional performances. I want to offer the community a variety of Indian dance experiences which include: group class and private tuition, school and preschool educational courses and workshops. dance theatre performances, community function workshops and performances, Kids Bollywood parties, wedding & conference performances, mouth percussion classes, Indian mythology/ dance costume and make up workshops.
The final design should communicate a feeling and impression of the vibrance and energy of Indian dance.
Updates
Hi Everyone,
Project Deadline Extended
Reason: I would like to refine a few changes to the details of this lovely design and we have run out of time!
Project Deadline Extended
Reason: Still waiting to hear back form designer re two possible changes to the card design. Tomorrow is the deadline and I have sent several messages but with no response. I need to see this through before selecting this lovely design.
Thank you.
Tessa
Industry/Entity Type
Preschool
Requirements
Must have
- The front of the business card should have the photo of me (my face and torso), surrounded entirely by a border of bright magenta (to match the magenta of my lipstick - it is the same as the magenta on my skirt in the second photo). Within the top border I want (perhaps yellow-gold) writing to say "Tessa Marlowe - Artistic Director" and within the bottom border it should read "Copper Lantern Indian Dance." If you turn the card on its side the left border should have my telephone number: 0417 862 049 and the right-hand border should read: copperlanternindiandance@velmora.com
The reverse of the card should be the orange of the dance costume
and I'd like the picture of my feet and legs to be on the right side of the back of the card as a side border. Centre-aligned on the orange background it should read (perhaps in dark magenta):
Indian dance classes + private tuition
School + preschool educational courses and workshops
Dance theatre performances
Community function workshops and performances
Children's Bollywood parties
Wedding + conference performances
Mouth percussion classes
Indian mythology and dance demonstration workshops
Dance costume and make-up workshops
Nice to have
- A lovely artistic but easy-to-read font would be nice.

```html
<!DOCTYPE html>
<html lang="en">
<head>
<meta charset="utf-8">
<title>Copper Lantern Indian Dance – Business Card</title>
<link href="https://fonts.googleapis.com/css2?family=Cinzel:wght@400;600&display=swap" rel="stylesheet">
<style>
  :root {
    --backdrop: #c9c9c9;
    --card-white: #ffffff;
    --card-grey: #e4e4e4;
    --gold-light: #e6bd45;
    --gold: #d2a027;
    --gold-deep: #b9871a;
    --magenta: #8a1d50;
    --saffron: #e9a126;
    --ink: #4a1616;
    --ink-soft: #2b2b2b;
  }
  * { box-sizing: border-box; margin: 0; padding: 0; }
  html, body {
    width: 1200px; height: 900px; overflow: hidden;
    background: var(--backdrop);
    font-family: "Cinzel", serif;
  }
  .canvas { position: relative; width: 1200px; height: 900px; }

  .card {
    position: absolute;
    width: 680px; height: 408px;
    overflow: hidden;
    background: linear-gradient(180deg, var(--card-white) 0%, var(--card-white) 55%, var(--card-grey) 100%);
  }
  .card--front { left: 80px; top: 36px; }
  .card--back  { left: 440px; top: 456px; }

  /* front */
  .front__band {
    position: absolute; left: 200px; right: 0; top: 12px; height: 100px;
    background: linear-gradient(180deg, var(--gold-light), var(--gold) 60%, var(--gold-deep));
  }
  .front__photo {
    position: absolute; left: 0; top: 0; width: 330px; height: 408px;
    background:
      radial-gradient(ellipse at 45% 40%, #e9c9b8 0%, rgba(233,201,184,0) 30%),
      linear-gradient(160deg, var(--saffron) 0%, #c9612e 45%, var(--magenta) 80%, #5e1236 100%);
    clip-path: polygon(0 0, 82% 0, 100% 40%, 88% 100%, 0 100%);
  }
  .front__title {
    position: absolute; left: 350px; right: 20px; top: 22px;
    text-align: center; color: #fff; font-variant: small-caps;
  }
  .front__name { font-size: 42px; font-weight: 600; letter-spacing: 2px; line-height: 46px; }
  .front__role { font-size: 32px; font-weight: 400; letter-spacing: 1px; line-height: 40px; }

  .front__brand {
    position: absolute; left: 330px; right: 0; top: 172px;
    text-align: center; color: var(--ink-soft);
  }
  .brand-dot {
    display: block; margin: 0 auto 10px; width: 30px; height: 30px;
    border-radius: 50%; background: var(--gold);
  }
  .brand-name { font-size: 19px; font-weight: 600; font-variant: small-caps; letter-spacing: .5px; }
  .front__phone { font-size: 34px; font-weight: 400; margin-top: 6px; letter-spacing: 1px; }
  .front__email { font-size: 14px; font-weight: 600; font-variant: small-caps; margin-top: 8px; letter-spacing: .3px; }

  /* back */
  .back__band {
    position: absolute; left: 0; top: 112px; width: 470px; height: 196px;
    background: linear-gradient(180deg, var(--gold-light), var(--gold) 60%, var(--gold-deep));
  }
  .back__services {
    position: absolute; left: 10px; top: 120px; width: 460px;
    list-style: none; text-align: center;
    color: var(--ink); font-size: 14px; font-weight: 600;
    font-variant: small-caps; line-height: 20px;
  }
  .back__photo {
    position: absolute; right: 0; top: 0; width: 250px; height: 408px;
    background: linear-gradient(200deg, #7a1a4b 0%, var(--magenta) 35%, var(--saffron) 70%, #c07a2a 100%);
    clip-path: polygon(22% 0, 100% 0, 100% 100%, 10% 100%, 0 55%);
  }
</style>
</head>
<body>
<main class="canvas">

  <section class="card card--front" aria-label="Business card front">
    <div class="front__band"></div>
    <div class="front__photo" role="img" aria-label="Photo of the dancer in gold and magenta classical Indian costume with flowers in her hair, framed by magenta swirl ornaments"></div>
    <header class="front__title">
      <h1 class="front__name">Tessa Marlowe</h1>
      <p class="front__role">Artistic Director</p>
    </header>
    <div class="front__brand">
      <span class="brand-dot"></span>
      <p class="brand-name">Copper Lantern Indian Dance</p>
      <p class="front__phone">0417 862 049</p>
      <p class="front__email">copperlanternindiandance@velmora.com</p>
    </div>
  </section>

  <section class="card card--back" aria-label="Business card back">
    <div class="back__band"></div>
    <ul class="back__services">
      <li>Indian dance classes + private tuition</li>
      <li>School + preschool educational courses and workshops</li>
      <li>Dance theatre performances</li>
      <li>Community function workshops and performances</li>
      <li>Children's Bollywood parties</li>
      <li>Wedding + conference performances</li>
      <li>Mouth percussion classes</li>
      <li>Indian mythology and dance demonstration workshops</li>
      <li>Dance costume and make-up workshops</li>
    </ul>
    <div class="back__photo" role="img" aria-label="Photo of the dancer's legs and feet in magenta and saffron costume with ankle bells, framed by magenta swirl ornaments"></div>
  </section>

</main>
</body>
</html>
```